依頼詳細
・基本的な掲載コンテンツは変更はありません。
・HTMLはすでに組んでありますので、デザインを製作を頂ければと思います。
・特にBODYのbackgroundイメージの変更は必須です。ベルモナタワーという高級マンションの1階にふさわしいデザインを希望します。
・サービスコンセプトは、高品質・高付加価値・高価格です。色はとりあえずワインレッドにしましたが、メインカラーはこだわりません。
・顧客イメージは30~50歳台、ペットを飼っている夫婦、直接購買者は女性(主婦)です。
・作成頂いたデザインをベースに他のページも制作したいと考えているため、その点も考慮して下さい。(サイトURLを参考にしてください)
サイトURL
http://kst.borimo.jp/
ページ数
1ページ
希望イメージ
シンプル 複雑
単色 カラフル
暗い 明るい
日常 高級
遊び心 厳粛
未来的 伝統的
女性的 男性的
希望する色
ワインレッド
納品ファイル
• イラストレーター形式 (.ai)
• フォトショップ形式 (.psd)
補足説明
店舗が入っているベルモナタワーのHPは下記になります。
http://www.terufisoven.net/
・フラッシュは使用不可

見やすさ、デザインの汎用性、フッターのオリジナリティなどが決定要因でした。

多くのご提案を頂きありがとうございました。

良い提案ばかりで、どれか決定するのに時間がかかりましたが、
今回はこちらのデザインに決めさせて頂きました。

また機会がありましたらどうぞ宜しくお願い致します。

```html
<!DOCTYPE html>
<html lang="ja">
<head>
<meta charset="utf-8">
<title>BRペット ベルモナタワー南台店</title>
<link href="https://fonts.googleapis.com/css2?family=Noto+Sans+JP:wght@400;700&family=Noto+Serif+JP:wght@500;700&display=swap" rel="stylesheet">
<style>
:root{
  --wine:#8a1c2c;
  --wine-dark:#6b1221;
  --beige:#e8dcc3;
  --beige-light:#f3ecdc;
  --sand:#d6c39c;
  --brown:#5a3a22;
  --text:#3b2e26;
  --muted:#7d6d5f;
  --white:#ffffff;
  --line:#c9b48b;
  --sns:#5b6f98;
}
*{margin:0;padding:0;box-sizing:border-box}
html,body{width:788px;height:1200px;overflow:hidden}
body{
  font-family:"Noto Sans JP",sans-serif;color:var(--text);
  background:linear-gradient(180deg,var(--beige-light) 0,var(--beige) 320px,#eadfca 1200px);
  position:relative;font-size:9px;
}
.abs{position:absolute}
.topline{left:14px;top:6px;font-size:8px;color:var(--brown);letter-spacing:.02em}
.brand{left:20px;top:22px;width:300px;height:74px;display:flex;align-items:center;gap:10px}
.brand-photo{width:72px;height:74px;border-radius:4px;background:radial-gradient(circle at 50% 45%,#f4eee4,#cdb896)}
.brand-name{font-family:"Noto Serif JP",serif;font-weight:700;color:var(--brown);font-size:30px;line-height:1}
.brand-sub{font-family:"Noto Serif JP",serif;font-weight:700;color:var(--brown);font-size:11px;margin-left:6px}
.reserve{left:582px;top:22px;width:192px;height:58px;background:var(--white);border:1px solid var(--line);text-align:center}
.reserve-label{background:var(--wine);color:var(--white);font-size:9px;padding:2px 0;font-weight:700}
.reserve-tel{font-size:20px;font-weight:700;color:var(--wine);display:flex;align-items:center;justify-content:center;gap:5px;margin-top:2px}
.reserve-hours{font-size:7.5px;color:var(--muted)}
.hero{left:12px;top:98px;width:764px;height:198px;background:linear-gradient(90deg,#efe5d0,#e2d2b1)}
.hero-photo{position:absolute;left:360px;top:4px;width:398px;height:190px;border-radius:3px;background:linear-gradient(120deg,#d9c3a0 0%,#b88a5c 45%,#f0e7da 70%,#c29a6c 100%)}
.service{position:absolute;left:88px;top:26px;width:150px;background:rgba(255,255,255,.92);border:1px solid var(--line)}
.service h2{background:var(--wine);color:var(--white);font-size:10px;text-align:center;padding:4px 0;font-family:"Noto Serif JP",serif}
.service ul{list-style:none;padding:6px 10px}
.service li{font-size:8.5px;padding:3px 0;color:var(--brown);border-bottom:1px dotted var(--line)}
.service li:before{content:"●";color:var(--wine);font-size:6px;margin-right:4px;vertical-align:middle}
.nav{left:12px;top:296px;width:764px;height:26px;background:linear-gradient(180deg,var(--wine),var(--wine-dark));display:flex}
.nav a{flex:1;color:var(--white);text-decoration:none;font-size:9px;display:flex;align-items:center;justify-content:center;border-right:1px solid rgba(255,255,255,.25)}
.nav a:last-child{border-right:0}
.content{left:12px;top:332px;width:764px;height:770px;background:var(--white)}
.sidebar{position:absolute;left:28px;top:30px;width:184px}
.side-item{height:56px;margin-bottom:4px;display:flex;border:1px solid var(--line)}
.side-photo{width:96px;background:linear-gradient(135deg,#d8c2a0,#a77a52)}
.side-label{flex:1;background:linear-gradient(90deg,var(--wine),var(--wine-dark));color:var(--white);font-size:9px;display:flex;align-items:flex-end;justify-content:flex-end;padding:5px}
.sns{margin-top:10px;border:1px solid #c8cfdc}
.sns-head{background:var(--sns);color:var(--white);font-size:8px;padding:3px 5px;font-weight:700}
.sns-body{padding:6px;font-size:7.5px;color:#444;line-height:1.5}
.sns-row{display:flex;gap:6px;align-items:center;margin:6px 0}
.sns-sq{width:30px;height:30px;background:#d4c6ae}
.sns-btn{display:inline-block;background:#e6e9f0;border:1px solid #bcc4d4;padding:1px 5px;font-size:7px}
.sns-avatars{display:flex;gap:4px;margin-top:5px}
.sns-avatars span{width:22px;height:22px;background:#cfd5e0}
.main{position:absolute;left:226px;top:26px;width:526px}
.title{font-family:"Noto Serif JP",serif;font-size:14px;color:var(--brown);border-bottom:2px solid var(--wine);padding:3px 0 4px 8px;position:relative}
.title:before{content:"";position:absolute;left:0;top:5px;width:3px;height:15px;background:var(--wine)}
.about{display:flex;gap:12px;margin-top:10px}
.building{width:98px;height:150px;background:linear-gradient(180deg,#b9cce0,#8d9aa8 60%,#6f6a64)}
.about p{font-size:8px;line-height:1.8;flex:1}
.sec{margin-top:14px;width:336px}
.sec h3{font-size:10px;color:var(--brown);border-bottom:1px solid var(--line);padding-bottom:3px;display:flex;align-items:center;gap:4px}
.sec h3:before{content:"";width:8px;height:8px;background:var(--wine)}
.sec p{font-size:8px;line-height:1.8;margin-top:4px}
.map{position:absolute;left:352px;top:232px;width:172px;height:265px;border:1px solid var(--line);background:linear-gradient(150deg,#f2f0ea,#dcdad2)}
.footer-links{left:0;top:1110px;width:788px;text-align:center;font-size:8px}
.footer-links a{color:var(--wine);text-decoration:none;margin:0 8px}
.copy{left:0;top:1142px;width:788px;text-align:center;font-size:7px;color:var(--muted)}
</style>
</head>
<body>
<p class="abs topline">BRペットベルモナタワー南台店 | ペットショップ・トリミングサロン・ペットホテル</p>

<div class="abs brand">
  <div class="brand-photo" role="img" aria-label="看板犬の写真"></div>
  <div><span class="brand-name">BRペット</span><span class="brand-sub">ベルモナタワー南台店</span></div>
</div>

<div class="abs reserve">
  <div class="reserve-label">ご予約</div>
  <div class="reserve-tel">
    <svg width="14" height="14" viewBox="0 0 24 24"><path fill="#8a1c2c" d="M6.6 10.8a15 15 0 0 0 6.6 6.6l2.2-2.2a1 1 0 0 1 1-.25 11.4 11.4 0 0 0 3.6.57 1 1 0 0 1 1 1V20a1 1 0 0 1-1 1A17 17 0 0 1 3 4a1 1 0 0 1 1-1h3.5a1 1 0 0 1 1 1c0 1.25.2 2.45.57 3.57a1 1 0 0 1-.25 1z"/></svg>
    03-5550-0142
  </div>
  <div class="reserve-hours">営業時間 10:00~19:30（年中無休）</div>
</div>

<div class="abs hero">
  <div class="hero-photo" role="img" aria-label="箱に並ぶ子犬たちの写真"></div>
  <div class="service">
    <h2>当社のサービス</h2>
    <ul>
      <li>子犬・子猫販売</li>
      <li>トリミング</li>
      <li>ペットホテル</li>
      <li>ペットフード・用品販売</li>
      <li>動物病院</li>
    </ul>
  </div>
</div>

<nav class="abs nav">
  <a href="#">TOP</a><a href="#">フード・用品</a><a href="#">サロン</a><a href="#">子犬・子猫</a><a href="#">ホテル</a><a href="#">動物病院</a><a href="#">アクセス</a>
</nav>

<div class="abs content">
  <aside class="sidebar">
    <div class="side-item"><div class="side-photo" role="img" aria-label="ペットフードの写真"></div><div class="side-label">フード・用品</div></div>
    <div class="side-item"><div class="side-photo" role="img" aria-label="トリミング中の犬の写真"></div><div class="side-label">サロン</div></div>
    <div class="side-item"><div class="side-photo" role="img" aria-label="子猫の写真"></div><div class="side-label">子犬・子猫</div></div>
    <div class="side-item"><div class="side-photo" role="img" aria-label="ホテルでくつろぐ犬の写真"></div><div class="side-label">ホテル</div></div>
    <div class="side-item"><div class="side-photo" role="img" aria-label="診察を受ける犬の写真"></div><div class="side-label">動物病院</div></div>
    <div class="sns">
      <div class="sns-head">ファンページ</div>
      <div class="sns-body">
        <div class="sns-row"><div class="sns-sq" role="img" aria-label="店舗アイコン"></div><div>BRペット ベルモナタワー南台店<br><span class="sns-btn">いいね！</span></div></div>
        <div>128人がいいねと言っています</div>
        <div class="sns-avatars"><span></span><span></span><span></span><span></span><span></span></div>
      </div>
    </div>
  </aside>

  <section class="main">
    <h1 class="title">BRペットについて</h1>
    <div class="about">
      <div class="building" role="img" aria-label="ベルモナタワーの外観写真"></div>
      <p>BRペットベルモナタワー南台店は、ベルモナタワー1階にある総合ペットショップです。<br>子犬・子猫の販売からトリミング、ペットホテル、動物病院まで、大切な家族のための上質なサービスをご用意しております。</p>
    </div>
    <div class="sec"><h3>営業時間</h3><p>10:00~19:30（年中無休）</p></div>
    <div class="sec"><h3>住所</h3><p>〒108-0071　東京都港区白浜2丁目 ベルモナタワー1階</p></div>
    <div class="sec"><h3>アクセス</h3><p>南台駅 徒歩3分<br>南台駅西口より徒歩5分</p></div>
    <div class="sec"><h3>駐車場</h3><p>営業時間 7:00~24:00 料金300円／30分<br>お買い上げ3,000円以上で1時間無料となります。</p></div>
    <div class="map" role="img" aria-label="店舗周辺の案内地図"></div>
  </section>
</div>

<nav class="abs footer-links">
  <a href="#">TOP</a><a href="#">フード・用品</a><a href="#">サロン</a><a href="#">子犬・子猫</a><a href="#">ホテル</a><a href="#">動物病院</a><a href="#">アクセス</a>
</nav>
<p class="abs copy">© 2012 BRペット ベルモナタワー南台店 All Rights Reserved.</p>
</body>
</html>
```